Introductory Flyer

We need a flyer to make businesses aware of our services. We do 3D Printing with a K540 Vantrix Printer(ie make solid prototypes from drawings.

We are a newish company looking to get new business. Photos and text can be taken from our website www.morlenfabworks.com.au and I have permision to use photos from www.vantrix.com if you need any extras. I could also write new text to suit your ideas.

3D Printing is a new technology.  People need to think "Hey! Look what this company can do for us."

Target Market(s)

Anyone designing or needing models of any solid object. Includes engineers, architects, councils, manufacturers. Need to send to businesses and get passed around rather than thrown out.

Industry/Entity Type

Manufacturing

Requirements
Must have
• Something quirky though not too expensive to print. Maybe folded popup card.

• Explain clearly what we actually do. ie 3D Printing and CAD Drawing.

• Not look out of accord with our website www.morlenfabworks.com.au

Nice to have
• Prefer smaller card to A4 sheet. Something to fit in DL envelope. Needs to convey quality and high tech side of our business.

```html
<!DOCTYPE html>
<html lang="en">
<head>
<meta charset="utf-8">
<title>Morlen Fabworks – Introductory Pop-up Card</title>
<link href="https://fonts.googleapis.com/css2?family=Source+Sans+3:ital,wght@0,400;0,600;0,700;0,900;1,900&display=swap" rel="stylesheet">
<style>
  :root {
    --orange: #f39020;
    --orange-deep: #e8801a;
    --white: #ffffff;
    --black: #0c0c0c;
    --stage: #434343;
    --ink: #2b2b2b;
    --shadow: rgba(0,0,0,0.35);
  }
  * { margin: 0; padding: 0; box-sizing: border-box; }
  html, body {
    width: 1200px; height: 600px; overflow: hidden;
    background: var(--stage);
    font-family: "Source Sans 3", "Myriad Pro", Arial, sans-serif;
  }
  .canvas { position: relative; width: 1200px; height: 600px; }

  /* shared card pieces */
  .card { position: absolute; background: var(--white); box-shadow: 8px 10px 0 var(--shadow); overflow: hidden; }
  .card svg.card-shapes { position: absolute; inset: 0; width: 100%; height: 100%; }

  /* cover */
  .cover { left: 55px; top: 60px; width: 375px; height: 190px; }
  .cover-title {
    position: absolute; left: 112px; top: 86px; width: 140px; text-align: center;
    color: var(--white); font-weight: 700; font-size: 11px; letter-spacing: 0.2px;
  }

  /* pop-up tab */
  .popup-tab { position: absolute; }
  .popup-tab svg { position: absolute; inset: 0; width: 100%; height: 100%; }
  .popup-slogan {
    position: absolute; left: 0; right: 0; text-align: center;
    color: var(--white); font-weight: 900; font-style: italic; line-height: 1.05;
  }
  .popup-photo {
    position: absolute;
    background: radial-gradient(ellipse at 50% 45%, #e9e6df 0%, #bdb9b0 45%, #1a1a1a 80%);
    border-radius: 3px;
  }
  .tab-front { left: 325px; top: 295px; width: 165px; height: 80px; }
  .tab-front .popup-slogan { top: 12px; font-size: 8.5px; }
  .tab-front .popup-photo { left: 58px; top: 40px; width: 56px; height: 36px; }

  .tab-inside { left: 800px; top: 52px; width: 180px; height: 86px; }
  .tab-inside .popup-slogan { top: 12px; font-size: 9px; }
  .tab-inside .popup-photo { left: 60px; top: 44px; width: 62px; height: 38px; }

  /* logo side */
  .logo-side { left: 210px; top: 372px; width: 370px; height: 192px; }
  .brand {
    position: absolute; left: 0; right: 0; top: 86px;
    display: flex; align-items: center; justify-content: center; gap: 8px;
  }
  .brand-mark { width: 16px; height: 16px; background: var(--orange); }
  .brand-name { color: var(--orange); font-weight: 700; font-size: 19px; letter-spacing: 0.3px; }

  /* inside spread */
  .inside { left: 685px; top: 135px; width: 400px; height: 385px; }
  .inside-top {
    position: absolute; left: 0; top: 0; width: 100%; height: 172px; background: var(--orange);
  }
  .specialty {
    position: absolute; left: 0; right: 0; top: 150px; text-align: center;
    color: var(--white); font-weight: 700; font-size: 13px; letter-spacing: 0.2px;
  }
  .photo { position: absolute; border: 2px solid var(--white); }
  .inside-bottom .photo { border-color: var(--orange); border-width: 3px; }
  .photo-light { background: linear-gradient(135deg, #f1efe9, #c9c3b6 60%, #8a2b2b); }
  .photo-dark { background: radial-gradient(ellipse at 50% 55%, #ece8de 0%, #b9b3a6 35%, #111 75%); }
  .photo-hands { background: linear-gradient(135deg, #f6f6f4 0%, #dcd9d3 55%, #2a2a2a 100%); }
  .photo-steel { background: linear-gradient(160deg, #d8d0c2, #b4ab9c 60%, #e8e6e2); }

  .copy { position: absolute; font-size: 7.2px; line-height: 1.22; }
  .copy p + p { margin-top: 4px; }
  .copy-top { left: 120px; top: 18px; width: 158px; color: var(--white); }
  .copy-top strong { font-weight: 700; }
  .copy-bottom { left: 128px; top: 186px; width: 150px; color: var(--orange-deep); }
  .apps-title { font-weight: 700; margin-top: 5px; font-size: 7.6px; }
  .apps { list-style: none; }
  .apps li::before { content: "◄ "; font-size: 6px; }

  .inside-corner { position: absolute; right: 0; bottom: 0; width: 130px; height: 55px; }
</style>
</head>
<body>
<main class="canvas">

  <!-- cover panel -->
  <section class="card cover">
    <svg class="card-shapes" viewBox="0 0 375 190" preserveAspectRatio="none" aria-hidden="true">
      <polygon points="300,0 375,0 375,32" fill="var(--orange)"/>
      <polygon points="0,135 0,190 75,190" fill="var(--orange)"/>
      <polygon points="108,0 255,0 252,150 218,190 140,190 104,140" fill="var(--orange)"/>
    </svg>
    <p class="cover-title">WELCOME TO...</p>
  </section>

  <!-- logo side with pop-up -->
  <div class="popup-tab tab-front">
    <svg viewBox="0 0 165 80" preserveAspectRatio="none" aria-hidden="true">
      <polygon points="28,12 125,0 165,14 142,80 0,80" fill="var(--orange)"/>
      <polygon points="38,20 122,8 152,20 132,80 14,80" fill="var(--black)"/>
    </svg>
    <p class="popup-slogan">Don't just think it!<br>Touch it!<br>See it 3D!</p>
    <div class="popup-photo" role="img" aria-label="Photo of a white 3D printed prototype part"></div>
  </div>
  <section class="card logo-side">
    <svg class="card-shapes" viewBox="0 0 370 192" preserveAspectRatio="none" aria-hidden="true">
      <polygon points="290,0 370,0 370,32" fill="var(--orange)"/>
      <polygon points="0,130 0,192 72,192" fill="var(--orange)"/>
    </svg>
    <div class="brand">
      <span class="brand-mark"></span>
      <span class="brand-name">Morlen Fabworks</span>
    </div>
  </section>

  <!-- inside spread -->
  <div class="popup-tab tab-inside">
    <svg viewBox="0 0 180 86" preserveAspectRatio="none" aria-hidden="true">
      <polygon points="34,10 140,0 180,14 156,86 0,86" fill="var(--orange)"/>
      <polygon points="44,18 136,8 166,20 144,86 16,86" fill="var(--black)"/>
    </svg>
    <p class="popup-slogan">Don't just think it!<br>Touch it!<br>See it 3D!</p>
    <div class="popup-photo" role="img" aria-label="Photo of a white 3D printed prototype part"></div>
  </div>

  <section class="card inside">
    <div class="inside-top">
      <div class="photo photo-light" style="left:20px;top:18px;width:90px;height:58px;" role="img" aria-label="Photo of a white architectural shopfront model"></div>
      <div class="photo photo-dark" style="left:22px;top:88px;width:88px;height:56px;" role="img" aria-label="Photo of a printed house model"></div>
      <div class="photo photo-hands" style="left:286px;top:18px;width:96px;height:58px;" role="img" aria-label="Photo of hands holding a printed part over a CAD drawing"></div>
      <div class="photo photo-steel" style="left:290px;top:88px;width:92px;height:56px;" role="img" aria-label="Photo of a printed bracket on stone"></div>
      <div class="copy copy-top">
        <p><strong>Get a head start</strong> in your design and sales process for that new product you've been thinking of. Morlen Fabworks offer a complete service including CAD drawing. You have the great idea. We'll make it reality.</p>
        <p>Using new 3D Printing technology we can jump start your design process by bringing amazing high definition 3D models into your hands quickly and affordably. These precision models are built up in very thin layers from computerised data such as a CAD drawing, an MRI scan or GIS data.</p>
      </div>
      <p class="specialty">Rapid Prototyping is our specialty!</p>
    </div>

    <div class="inside-bottom">
      <div class="photo photo-dark" style="left:28px;top:186px;width:92px;height:64px;" role="img" aria-label="Photo of a printed surgical instrument"></div>
      <div class="photo photo-dark" style="left:24px;top:262px;width:92px;height:64px;" role="img" aria-label="Photo of a printed jaw bone model"></div>
      <div class="photo photo-dark" style="left:294px;top:196px;width:86px;height:150px;" role="img" aria-label="Photo of a printed statue model"></div>
      <div class="copy copy-bottom">
        <p>Morlen Fabworks serves local, national and international clients. We treat your information with complete confidentiality.</p>
        <p>In addition to directly printed models we can also provide you with moulded urethane or plastic models. You don't have to have your own CAD data to get models made at Morlen Fabworks. We offer a complete CAD Drawing service. All you need is the idea!</p>
        <p class="apps-title">Some Common Applications</p>
        <ul class="apps">
          <li>Surgical Instrument Design</li>
          <li>Injection Moulded Parts</li>
          <li>Blanks for Sand Cast Moulds</li>
          <li>Extruded or Moulded Profiles</li>
        </ul>
      </div>
      <svg class="inside-corner" viewBox="0 0 130 55" preserveAspectRatio="none" aria-hidden="true">
        <polygon points="130,0 130,55 40,55" fill="var(--orange)"/>
      </svg>
    </div>
  </section>

</main>
</body>
</html>
```